Flyer-Design für Mittagsbelieferung
Zielgruppe
Mittags Belieferung ältere Menschen, Firmen, Berufstätige
Aufgabenstellung
Text aus Datei den Bestellzettel nicht weiter beachten nur Seite 2 u.3... Logo vielleicht vorne drauf... Format bin ich unentschieden

```html
<!DOCTYPE html>
<html lang="de">
<head>
<meta charset="utf-8">
<title>lumo bringt's – Flyer</title>
<link rel="stylesheet" href="https://fonts.googleapis.com/css2?family=Open+Sans:wght@400;600;700;800&display=swap">
<style>
  :root{
    --green:#3fae3f;
    --green-dark:#2f8f31;
    --paper:#ecebe8;
    --paper-line:#dedcd7;
    --ink:#2b2b2b;
    --white:#ffffff;
    --stage:#f1f1f1;
  }
  *{box-sizing:border-box;margin:0;padding:0}
  html,body{width:1200px;height:800px;overflow:hidden;background:var(--stage);font-family:"Open Sans",Arial,sans-serif;color:var(--ink)}
  .spread{position:relative;width:1200px;height:800px;display:flex;gap:40px;justify-content:center;align-items:center}
  .page{position:relative;width:540px;height:764px;overflow:hidden;
    background:repeating-linear-gradient(90deg,var(--paper) 0 14px,var(--paper-line) 14px 15px,var(--paper) 15px 31px,#e4e2de 31px 32px);
    box-shadow:0 6px 18px rgba(0,0,0,.12)}

  /* front */
  .photo{position:absolute;border-radius:50%;box-shadow:0 4px 10px rgba(0,0,0,.25);transform:translate(-50%,-50%)}
  .photo--stew{width:230px;height:230px;left:520px;top:10px;background:radial-gradient(circle,#8a6a3c 0,#5e4a2a 55%,#262624 62%,#1d1d1d 100%)}
  .photo--wedges{width:200px;height:200px;left:545px;top:420px;background:radial-gradient(circle,#c9622a 0,#a84a22 45%,#6c8a3a 70%,#c9b89a 72%,#b8a88a 100%)}
  .photo--soup{width:210px;height:210px;left:0;top:390px;background:radial-gradient(circle,#efe6d2 0,#d9c7a0 35%,#b98a4e 50%,#a47a45 100%)}
  .photo--seafood{width:260px;height:260px;left:40px;top:790px;background:radial-gradient(circle,#c46a3e 0,#8a4a2e 45%,#3f5a30 65%,#262624 72%,#1c1c1c 100%)}

  .band{position:absolute;background:var(--green);color:var(--white);text-align:center;transform:translate(-50%,-50%) rotate(45deg);z-index:2}
  .band--price{width:520px;left:420px;top:118px;padding:8px 0 10px}
  .band--price .price{font-size:32px;font-weight:700;line-height:1.1}
  .band--price .note{font-size:16px;line-height:1.3}
  .band--cake{width:560px;left:118px;top:648px;padding:6px 0 8px;font-size:17px;line-height:1.22}
  .band--cake strong{font-weight:700}
  .band--cake .cake-price{font-size:23px;font-weight:700}

  .logo-card{position:absolute;left:120px;top:232px;width:300px;height:300px;background:var(--white);z-index:1;
    display:flex;flex-direction:column;align-items:center;justify-content:center;gap:10px;box-shadow:0 2px 6px rgba(0,0,0,.08)}
  .brand{display:flex;align-items:center;gap:8px;font-size:30px;font-weight:800;color:var(--green)}
  .brand-dot{width:14px;height:14px;border-radius:50%;background:var(--green)}
  .tagline{font-size:13px;font-weight:700;color:var(--ink)}
  .mascot{width:150px;height:120px;border-radius:10px;background:radial-gradient(circle at 50% 45%,#f08a2c 0,#c8321f 60%,#e8e8e8 100%)}
  .front-phone{font-size:24px;font-weight:700;letter-spacing:.5px}

  /* back */
  .page--back{padding:30px 38px;display:flex;flex-direction:column;align-items:center;text-align:center;font-size:12.5px;line-height:1.45}
  .intro{margin-bottom:10px}
  .hl{color:var(--green);font-weight:700}
  .pay-title{font-weight:700;margin-bottom:6px}
  .pay-block{margin-bottom:8px}
  .delivery{font-weight:600;margin-bottom:14px}
  .area{background:var(--green);color:var(--white);width:calc(100% + 76px);padding:12px 40px;font-size:13px;margin-bottom:14px}
  .invite{margin-bottom:14px}
  .contract-box{border:2px solid var(--green);width:100%;padding:14px 18px;margin-bottom:18px}
  .contract-box h2{font-size:20px;font-weight:700;margin-bottom:6px}
  .contract-box p{font-size:11.5px}
  .contact-row{display:flex;align-items:center;gap:26px;width:100%}
  .mascot--small{width:110px;height:90px;flex:none}
  .contact{text-align:left}
  .contact h3{font-size:15px;font-weight:700;margin-bottom:6px}
  .contact-line{display:flex;align-items:center;gap:8px;font-size:14px;font-weight:700;margin-bottom:4px}
  .contact-line svg{width:18px;height:18px;flex:none}
</style>
</head>
<body>
<main class="spread">

  <section class="page page--front">
    <div class="photo photo--stew" role="img" aria-label="Foto: Schmorgericht mit Gemüse in schwarzer Schale"></div>
    <div class="photo photo--wedges" role="img" aria-label="Foto: Kartoffelspalten mit Salat und Dip"></div>
    <div class="photo photo--soup" role="img" aria-label="Foto: Pilzsuppe im Brotlaib"></div>
    <div class="photo photo--seafood" role="img" aria-label="Foto: Meeresfrüchte-Pfanne mit Kräutern"></div>

    <div class="band band--price">
      <div class="price">6,00€/Menü</div>
      <div class="note">inkl. Nachtisch und Lieferung</div>
    </div>

    <div class="logo-card">
      <div class="brand"><span class="brand-dot"></span>lumo bringt's</div>
      <div class="tagline">ihr mobiler Mittagstisch aus Lindhagen</div>
      <div class="mascot" role="img" aria-label="Illustration: Maskottchen auf rotem Motorroller mit Essen"></div>
      <div class="front-phone">04821/5573920</div>
    </div>

    <div class="band band--cake">
      <strong>1 Stück<br>selbstgebackenen</strong><br>
      Kuchen liefern wir<br>ihnen gerne für<br>
      <span class="cake-price">1,50€</span> mit dazu
    </div>
  </section>

  <section class="page page--back">
    <p class="intro">Wir liefern ihnen gerne ihr Wunschmenü in unseren Thermoboxen zu ihnen nachhause oder auch ins Büro oder an ihren Arbeitsplatz. Sie haben täglich die Wahl zwischen <span class="hl">3 Menüs inkl. Nachtisch.</span></p>
    <p class="pay-title">Bei der Bezahlung haben Sie die Wahl zwischen:</p>
    <p class="pay-block"><span class="hl">Barzahlung:</span><br>immer Montags im Vorraus beim Fahrer gegen<br>Erhalt der Wochenrechnung</p>
    <p class="pay-block"><span class="hl">Monatsrechnung:</span><br>am Ende des Monats wird ihnen eine Rechnung für den jeweiligen<br>Monat ausgestellt die Sie dann einfach überweisen.</p>
    <p class="delivery">Auslieferung erfolgt von Montag - Samstag<br>zwischen 10.30Uhr und 12.30Uhr</p>
    <p class="area">Derzeitiges Auslieferungsgebiet Lindhagen-Moorwitz-Tessenhof-Klarbeck-Wendelin-Rohrsdorf-Fennow-Seestadt-Altheide-Brinkau-Sellmin auch weitere möglich</p>
    <p class="invite">Fordern sie noch heute einen Speiseplan von uns an, und überzeugen<br>Sie sich von unseren täglich frisch zubereiteten Speisen.</p>
    <div class="contract-box">
      <h2>Keine Vertragsbindung!!</h2>
      <p>d.h. Sollte es ihnen nicht gefallen können Sie jederzeit wieder abbestellen.<br>An-und Abbestellungen sind täglich bis 10.00Uhr möglich.</p>
    </div>
    <div class="contact-row">
      <div class="mascot mascot--small" role="img" aria-label="Illustration: Maskottchen auf rotem Motorroller"></div>
      <div class="contact">
        <h3>Bestellhotline:</h3>
        <div class="contact-line">
          <svg viewBox="0 0 24 24" aria-hidden="true"><path fill="var(--green)" d="M6.6 10.8a15.1 15.1 0 0 0 6.6 6.6l2.2-2.2c.3-.3.7-.4 1-.2 1.1.4 2.3.6 3.6.6.6 0 1 .4 1 1V20c0 .6-.4 1-1 1A17 17 0 0 1 3 4c0-.6.4-1 1-1h3.5c.6 0 1 .4 1 1 0 1.3.2 2.5.6 3.6.1.3 0 .7-.2 1z"/></svg>
          04821/5573920
        </div>
        <div class="contact-line">
          <svg viewBox="0 0 24 24" aria-hidden="true"><rect x="2" y="5" width="20" height="14" rx="2" fill="var(--green)"/><path d="M3 6l9 7 9-7" fill="none" stroke="#fff" stroke-width="2"/></svg>
          bestellung@lumo-mittag.de
        </div>
      </div>
    </div>
  </section>

</main>
</body>
</html>
```